Flyer-Design für verschiedene Anwendungsfälle bzw. Produkte
Zielgruppe
Wir lösen reale Probleme mit digitalen Technologien wie IoT und KI. In unseren Projekten liefern wir Gesamtlösungen von der Strategieberatung über Konzepterstellung bis zur technischen Umsetzung und dem Betrieb. Integration und Konzeption spielen eine große Rolle, wir sind kein Hardwareanbieter, sondern bauen Komplettlösungen aus Software, Connectivity und Hardware. Unsere Kunden sind gehobener Mittelstand bis Konzern, ab 25 Mio € aufwärts. Oft sind unsere Kunden aus konservativen Branchen. Wir müssen beim Design immer einen Kompromiss aus innovativ und Vertrauen erweckend finden. Unsere Persona ist weiß, männlich, über 50, nicht besonders technologieaffin.
Aufgabenstellung
Wir brauchen eine Flyer-Vorlage für verschiedene Anwendungsfälle bzw. Produkte. Im Anhang sind Beispiele für Produktbeschreibungen, sowie ein Flyer, den wir selbst designet haben.
Ergebnis soll ein Flyer-Design sein, das wir für solche Produkte immer wieder verwenden können, DIN A5 zweiseitig.
Exo2 und Trebuchet sind unsere Schriftarten. Logos habe ich in 2 Formaten angehängt.
Website: tavolu.me
Wenn Sie weitere Ideen haben, sind wir ganz Ohr.
Grafisch bitte nur die Farben grau, schwarz und orange verwenden (grau und orange siehe Logo)

```html
<!DOCTYPE html>
<html lang="de">
<head>
<meta charset="utf-8">
<title>Flyer Füllstandsüberwachung</title>
<link rel="stylesheet" href="https://fonts.googleapis.com/css2?family=Montserrat:wght@400;500;600;700;800&display=swap">
<style>
  :root {
    --orange: #e8781e;
    --navy: #1f2a3d;
    --navy-soft: #3a475c;
    --ink: #151515;
    --grey-text: #3b3b3b;
    --paper: #ffffff;
    --backdrop: #e4e4e4;
  }
  * { box-sizing: border-box; margin: 0; padding: 0; }
  html, body { width: 1200px; height: 900px; overflow: hidden; }
  body {
    background: var(--backdrop);
    font-family: "Montserrat", sans-serif;
    position: relative;
  }
  .flyer {
    position: absolute;
    top: 60px;
    width: 552px;
    height: 780px;
    background: var(--paper);
    overflow: hidden;
    box-shadow: 0 6px 22px rgba(0,0,0,.15);
  }
  .flyer--front { left: 28px; }
  .flyer--back { left: 620px; }

  /* front */
  .hero-pattern {
    position: absolute; left: 0; top: 0; width: 100%; height: 310px;
    background: radial-gradient(ellipse at 55% 40%, #d9d9d9 0%, #f2f2f2 55%, #fafafa 100%);
  }
  .headline {
    position: absolute; left: 44px; top: 50px;
    font-weight: 800; font-size: 42px; line-height: 1.05; color: var(--ink);
  }
  .subline {
    position: absolute; left: 44px; top: 190px;
    font-weight: 700; font-size: 20px; line-height: 1.3; color: var(--orange);
  }
  .brand {
    position: absolute; right: 40px; top: 190px;
    display: flex; align-items: center; gap: 8px;
    font-weight: 600; font-size: 28px; letter-spacing: 4px; color: var(--orange);
  }
  .brand-dot { width: 11px; height: 11px; border-radius: 50%; background: var(--orange); }
  .case-band {
    position: absolute; left: 0; top: 258px; width: 100%; height: 160px;
  }
  .case-band svg { position: absolute; inset: 0; width: 100%; height: 100%; }
  .case {
    position: absolute; width: 240px; color: #fff;
    font-size: 13px; line-height: 1.4;
  }
  .case--one { left: 40px; top: 318px; }
  .case--two { left: 290px; top: 276px; }
  .case-label { font-weight: 700; font-size: 14px; margin-bottom: 3px; }
  .benefits-panel {
    position: absolute; left: 0; top: 405px; width: 100%; height: 300px;
    background: linear-gradient(135deg, var(--navy) 0%, var(--navy) 55%, var(--navy-soft) 100%);
  }
  .benefits {
    position: absolute; top: 420px; width: 240px; list-style: none;
    color: #fff; font-size: 13px; line-height: 1.4;
  }
  .benefits--one { left: 40px; }
  .benefits--two { left: 290px; }
  .footer-band { position: absolute; left: 0; bottom: 0; width: 100%; height: 100px; }
  .footer-band svg { position: absolute; inset: 0; width: 100%; height: 100%; }
  .contact {
    position: absolute; color: #fff; font-size: 12px; line-height: 16px;
    display: flex; align-items: center; gap: 7px; white-space: nowrap;
  }
  .contact svg { width: 16px; height: 16px; flex: none; }
  .contact--address { left: 215px; bottom: 42px; }
  .contact--mobile { left: 215px; bottom: 16px; }
  .contact--mail { left: 375px; bottom: 16px; }
  .contact--phone { left: 30px; bottom: 12px; }

  /* back */
  .back-top { position: absolute; left: 0; top: 0; width: 100%; height: 34px; background: var(--navy); }
  .back-bottom {
    position: absolute; left: 0; bottom: 0; width: 100%; height: 52px;
    background: var(--orange);
    display: flex; align-items: center; justify-content: center;
    color: #fff; font-weight: 700; font-size: 15px;
  }
  .back-content {
    position: absolute; left: 40px; right: 40px; top: 50px;
    text-align: center; color: var(--grey-text); font-size: 11.5px; line-height: 1.45;
  }
  .section-tag {
    display: inline-block; background: var(--orange); color: #fff;
    font-weight: 700; font-size: 14px; padding: 3px 12px; margin: 0 auto 8px;
  }
  .section-tag--wide { font-size: 15px; }
  .section-text p { margin-bottom: 5px; }
  .hardware-box {
    border: 1.5px solid var(--orange); margin: 22px 14px 22px; padding: 0 18px 18px;
  }
  .hardware-box .section-tag { margin-top: -12px; }
  .sensor-row { display: flex; justify-content: space-around; align-items: center; margin-top: 14px; }
  .sensor-shot { width: 80px; height: 50px; border-radius: 10px; background: linear-gradient(160deg, #5a5a5a, #1c1c1c); }
  .sensor-shot--mid { width: 74px; height: 56px; background: linear-gradient(160deg, #4a4a4a 0%, #2a8f86 60%, #1c1c1c 100%); }
</style>
</head>
<body>

<section class="flyer flyer--front" aria-label="Vorderseite">
  <div class="hero-pattern" role="img" aria-label="Hellgraue Netzwerkgrafik aus verbundenen Punkten und Linien"></div>
  <h1 class="headline">LoRaWAN<br>oder<br>NB-IoT:</h1>
  <p class="subline">Füllstandsüberwachung<br>und Routenoptimierung<br>Abfallwirtschaft</p>
  <div class="brand"><span class="brand-dot"></span>TAVOLU</div>

  <div class="case-band">
    <svg viewBox="0 0 552 160" preserveAspectRatio="none">
      <polygon points="0,44 552,0 552,160 0,160" fill="var(--orange)"/>
    </svg>
  </div>
  <div class="case case--one">
    <p class="case-label">Fall 1:</p>
    <p>große öffentliche Container, z.B. Altglas, Altkleider, Altpapier Nutzen und Vorteile</p>
  </div>
  <div class="case case--two">
    <p class="case-label">Fall 2:</p>
    <p>Kleinere städtische Mülleimer, z.B. in Erholungsgebieten Nutzen und Vorteile</p>
  </div>

  <div class="benefits-panel"></div>
  <ul class="benefits benefits--one">
    <li>- Bürger wissen, zu welchen Containern sie ihren Abfall bringen können</li>
    <li>- Entsorger kann optimiert leeren und Kosten sparen</li>
    <li>- Containerstandorte können datengestützt erweitert oder reduziert werden</li>
    <li>- Weniger wilder Müll</li>
  </ul>
  <ul class="benefits benefits--two">
    <li>- Nutzung der Mülleimer ist stark von unregelmäßigen Faktoren wie Wetter oder Veranstaltungen abhängig</li>
    <li>- Starr regelmäßige Leerung führt häufig zu Überfüllung und dadurch Umweltverschmutzung, die durch die Anwendung von Sensoren vermieden wird</li>
    <li>- Überflüssige Leerungen werden vermieden und dadurch Kosten gespart</li>
  </ul>

  <div class="footer-band">
    <svg viewBox="0 0 552 100" preserveAspectRatio="none">
      <polygon points="0,0 552,0 552,100 0,100" fill="var(--navy)"/>
      <polygon points="0,60 185,60 200,30 552,30 552,100 0,100" fill="var(--orange)"/>
    </svg>
  </div>
  <p class="contact contact--address">
    <svg viewBox="0 0 16 16"><circle cx="8" cy="8" r="8" fill="#fff"/><path d="M4 8.5 8 5l4 3.5V12H9.5V9.5h-3V12H4z" fill="var(--orange)"/></svg>
    Hafenweg 12, 40210, Musterstadt
  </p>
  <p class="contact contact--mobile">
    <svg viewBox="0 0 16 16"><circle cx="8" cy="8" r="8" fill="#fff"/><rect x="5.5" y="3.5" width="5" height="9" rx="1" fill="var(--orange)"/></svg>
    +49 170 5550123
  </p>
  <p class="contact contact--mail">
    <svg viewBox="0 0 16 16"><circle cx="8" cy="8" r="8" fill="#fff"/><rect x="4" y="5" width="8" height="6" fill="var(--orange)"/><path d="M4 5l4 3.5L12 5" stroke="#fff" fill="none"/></svg>
    consulting@tavolu.me
  </p>
  <p class="contact contact--phone">
    <svg viewBox="0 0 16 16"><circle cx="8" cy="8" r="8" fill="#fff"/><path d="M5 4.5c0 4 2.5 6.5 6.5 6.5l.5-1.8-2-1-1 1c-1-.5-2-1.5-2.5-2.5l1-1-1-2z" fill="var(--orange)"/></svg>
    0211 5550140
  </p>
</section>

<section class="flyer flyer--back" aria-label="Rückseite">
  <div class="back-top"></div>
  <div class="back-content">
    <h2 class="section-tag">Funktionsweise</h2>
    <div class="section-text">
      <p>- Im Container werden Sensoren zur Füllstandsmessung angebracht.</p>
      <p>- Der Füllstand wird an eine Bürger-Website/ -App gemeldet, die nur „voll“, „fast voll“ und „nicht voll“ anzeigt, sowie bei voll oder fast voll eine möglichst nahe gelegene Alternative.</p>
      <p>- Der Füllstand wird an den Entsorger gemeldet. Hier kann entweder eine Routenoptimierungs-App zur Verfügung gestellt oder die Daten in ein bestehendes Betriebsführungssystem integriert werden.</p>
      <p>- Die Daten werden analysiert, um die regelmäßige Auslastung der Container zu bestimmen und ihre Standorte langfristig zu optimieren.</p>
    </div>

    <div class="hardware-box">
      <h2 class="section-tag">Hardware</h2>
      <p>Ultraschall-, Radar- oder optische Sensoren messen den Abstand zwischen sich selbst und der Oberfläche und erkennen so den Füllstand</p>
      <div class="sensor-row">
        <div class="sensor-shot" role="img" aria-label="Foto zweier kompakter schwarzer Füllstandssensoren"></div>
        <div class="sensor-shot sensor-shot--mid" role="img" aria-label="Foto eines Sensors mit türkisfarbener Messfläche"></div>
        <div class="sensor-shot" role="img" aria-label="Foto eines flachen schwarzen Radarsensors"></div>
      </div>
    </div>

    <h2 class="section-tag section-tag--wide">Frontend und Benachrichtigungen</h2>
    <div class="section-text">
      <p>- Darstellung in einer Web App (für Mobilgeräte und PCs) auf einer Karte für Bürger, mit Anzeige von Alternativen bei vollen Containern</p>
      <p>- Einbindung in Routenoptimierungs- oder Betriebsführungs-Anwendung beim Entsorger</p>
      <p>- Alarmierung bei Überschreitung von Grenzwerten möglich</p>
    </div>
  </div>
  <div class="back-bottom">www.tavolu.me</div>
</section>

</body>
</html>
```